Business Card & Logo Design - Hedge Fund

We need a business card and logo design for a hedge fund. The hedge fund is named Morvane Holdings LLC. Morvane Holdings was created by finance professors and the strategy is based academic research that looks for patterns in stock prices. The design should look conservative, solid, strong. We favor a classic style - nothing flashy. The logo can relate to the name Morvane Holdings, or it could involve a symbol design that connotes "science" . We are open to ideas. We do not want alot of colors - but if any, color - blue is preferred. The font that seems to look best for the name (Morvane Holdings) is arial black. We are open to ideas. Most important - we want to see a mock up of an actual business card with the logo concept embedded. The business card should include space for : company name, individual name, position title, cell phone, address. We hope to have this work done by Sept. 8.

Target Market(s)

We will be meeting with and giving the business card to institutions and high net worth individuals.

Industry/Entity Type

Investment Advisory

Contact Information for Business Card

Company name - Morvane Holdings LLC
Individual name - Peter Vosk
Title - Portfolio Manager
Cell - (482) 555-0137
Address - 2750 Birchwell Lane, Suite 300, Atlanta GA 30327

Font styles to use
Other font styles liked:
• Arial

Colors
3277b5
0255a3
85acd3
cedeed
fdf9cf
d9d9d9
e6e6e6
f04a50
6b449b

Requirements
Must have
• Must have card details that are sited above.
• We would like a logo related to the name (Morvane Holdings) or concept of the fund.
Nice to have
• We want conservative / understated / clean crisp look.
• If any colors - we prefer conservative appearance - blue / gray.
• I have enclosed an example of a card style that looks attractive - please do not exactly copy this card. This is not our company or logo. I feel the layout is attractive - just as an example
Should not have
• Avoid too much color.
• I have selected some preferred colors. Please do not use all of the colors - I have selected a few that might work - but I am not sure. We are open to your ideas so please do not feel the need to use all or any of these.

```html
<!DOCTYPE html>
<html lang="en">
<head>
<meta charset="utf-8">
<title>Morvane Holdings – Business Card</title>
<link rel="stylesheet" href="https://fonts.googleapis.com/css2?family=Arimo:wght@400;700&display=swap">
<style>
  :root {
    --stage: #e6e6e6;
    --brand-blue: #0255a3;
    --accent-blue: #3277b5;
    --soft-blue: #85acd3;
    --pale-blue: #cedeed;
    --card-white: #f7f7f5;
    --ink: #4a4a4a;
    --rule: #8a8a8a;
  }
  * { box-sizing: border-box; margin: 0; padding: 0; }
  html, body { width: 1200px; height: 1200px; overflow: hidden; }
  body {
    background: var(--stage);
    font-family: "Arimo", Arial, sans-serif;
    display: flex;
    flex-direction: column;
    align-items: center;
    justify-content: center;
    gap: 70px;
  }
  .card {
    width: 700px;
    height: 400px;
    position: relative;
    box-shadow: 0 6px 18px rgba(0,0,0,0.12);
  }
  .card-back {
    background: var(--brand-blue);
    display: flex;
    align-items: center;
    justify-content: center;
  }
  .card-back .pattern {
    position: absolute;
    inset: 0;
    background: linear-gradient(135deg, #0a5cab 0%, var(--brand-blue) 50%, #0a5cab 100%);
  }
  .card-back .brand {
    position: relative;
    display: flex;
    align-items: center;
    gap: 16px;
    color: var(--soft-blue);
    font-weight: 700;
    font-size: 40px;
  }
  .brand-dot {
    width: 18px; height: 18px; border-radius: 50%;
    background: currentColor;
  }
  .card-front {
    background: var(--card-white);
    display: flex;
    align-items: center;
    padding: 0 48px 0 56px;
  }
  .card-front .brand {
    width: 220px;
    display: flex;
    align-items: center;
    gap: 12px;
    color: var(--accent-blue);
    font-weight: 700;
    font-size: 26px;
    line-height: 1.15;
  }
  .card-front .brand .brand-dot { width: 14px; height: 14px; flex: none; }
  .divider {
    width: 2px;
    height: 200px;
    background: var(--rule);
    margin: 0 36px 0 24px;
  }
  .details { color: var(--ink); }
  .person-name {
    color: var(--accent-blue);
    font-weight: 700;
    font-size: 34px;
    line-height: 1.1;
  }
  .person-title { font-size: 26px; margin-bottom: 22px; }
  .contact { font-size: 25px; line-height: 1.3; }
</style>
</head>
<body>
  <section class="card card-back">
    <div class="pattern" role="img" aria-label="Faint line pattern in light blue across the card back"></div>
    <div class="brand"><span class="brand-dot"></span>Morvane Holdings</div>
  </section>

  <section class="card card-front">
    <div class="brand"><span class="brand-dot"></span>Morvane Holdings</div>
    <div class="divider"></div>
    <div class="details">
      <p class="person-name">Peter Vosk</p>
      <p class="person-title">Portfolio Manager</p>
      <p class="contact">Cell - (482) 555-0137</p>
      <p class="contact">2750 Birchwell Lane,</p>
      <p class="contact">Suite 300, Atlanta GA 30327</p>
    </div>
  </section>
</body>
</html>
```